Yoga Training Cerificate

Design a certificate of graduation from a Vinyasa Yoga Teacher Training Program.

The attached document is an example of the certificate I received as a graduate from a teacher training program. You can use it as a template.

Stylistically, what you design can be: visually enticing, professional, clean, and modern.

Please develop the "Tidal Lotus" logo and embed it within the certificate.

Please add a circular watermark behind the body of the certificate similar to the one found in the attachment; leave out the words Asana Guild because I am not associated with that organization.

The name of my school is "Tidal Lotus." And it was established in 2017, which you can include.

The certificate affirms that "' 'such-and-such' has successfully completed the Tidal Lotus modern vinyasa yoga training, completing two hundred hours of instruction in practice and theory. Within the power of our institution as a certifying agent we declare Such-and-such, now, a teacher competent to share the gift of yoga with the masses in a safe and effective."

My name -Dennis Halvorsen- should be at bottom with a faux-signature; position title: Tidal Lotus founder.

If you decide to include text on the fringe, like the example, it might include bars of text describing the maxims of the Tidal Lotus school reading:

This is Tidal Lotus
Breath is primary
Evolve the physical culture
Bring your unique expression to the practice
Take Breaks
Freestyle
Close your eyes
Feel deeper into your body
This is active meditation
This is moving meditation
This is modern meditation

And find a way to integrate Emojis like: Fire, Water, Prayer Hands, etc. as you see fit.

Generally, make the certificate look: official, clear and clean. You can base it from the example given. And try and create a graphic design that is more visually capturing then the example.

```html
<!DOCTYPE html>
<html lang="en">
<head>
<meta charset="utf-8">
<title>Tidal Lotus — Certificate of Completion</title>
<link rel="stylesheet" href="https://fonts.googleapis.com/css2?family=Crimson+Text:ital@1&family=Mrs+Saint+Delafield&family=Open+Sans:ital,wght@0,400;1,400&family=Pinyon+Script&display=swap">
<style>
  :root {
    --paper: #efece6;
    --paper-edge: #e6e2da;
    --ink: #2b2b2b;
    --ink-soft: #4a4a4a;
    --rule: #1e1e1e;
    --fill-line: #9a9a9a;
    --mark: rgba(120, 118, 112, 0.16);
    --mark-ring: rgba(120, 118, 112, 0.22);
    --seal: #b3121a;
    --seal-dark: #7d0a10;
    --seal-light: #e03a3f;
  }
  html, body {
    margin: 0;
    padding: 0;
    width: 1200px;
    height: 848px;
    overflow: hidden;
    background: var(--paper);
  }
  .certificate {
    position: relative;
    width: 1200px;
    height: 848px;
    overflow: hidden;
    background: radial-gradient(ellipse at 50% 45%, var(--paper) 55%, var(--paper-edge) 100%);
    font-family: "Open Sans", Arial, sans-serif;
    color: var(--ink);
  }
  .school-mark {
    position: absolute;
    left: 0;
    top: 0;
  }
  .maxims {
    position: absolute;
    left: 73px;
    top: 186px;
    margin: 0;
    padding: 0;
    list-style: none;
    width: 240px;
    font-size: 16px;
    line-height: 20px;
    color: var(--ink-soft);
  }
  .maxims li { margin-bottom: 21px; }
  .maxims li.two-line { margin-bottom: 21px; }
  .divider {
    position: absolute;
    left: 366px;
    top: 142px;
    width: 3px;
    height: 528px;
    background: var(--rule);
  }
  .brand {
    position: absolute;
    left: 90px;
    top: 690px;
    width: 160px;
    text-align: center;
  }
  .brand-dot {
    display: block;
    width: 56px;
    height: 56px;
    margin: 0 auto 14px;
    border-radius: 50%;
    background: var(--ink);
  }
  .brand-name {
    font-family: "Open Sans", Arial, sans-serif;
    font-size: 26px;
    color: var(--ink);
    white-space: nowrap;
  }
  .title {
    position: absolute;
    left: 0;
    top: 0;
  }
  .title text {
    font-family: "Pinyon Script", cursive;
    font-size: 86px;
    fill: #3a3a3a;
  }
  .date-line {
    position: absolute;
    left: 534px;
    top: 242px;
    font-family: "Crimson Text", Georgia, serif;
    font-style: italic;
    font-size: 29px;
    color: var(--ink);
    white-space: nowrap;
  }
  .blank {
    display: inline-block;
    border-bottom: 1px solid var(--fill-line);
    vertical-align: baseline;
    height: 4px;
  }
  .blank.day { width: 110px; margin: 0 6px; }
  .blank.month { width: 68px; margin: 0 4px; }
  .blank.year { width: 60px; margin: 0 2px 0 8px; }
  .name-line {
    position: absolute;
    left: 475px;
    top: 449px;
    width: 693px;
    height: 1px;
    background: var(--ink-soft);
  }
  .statement {
    position: absolute;
    left: 520px;
    top: 470px;
    width: 590px;
    margin: 0;
    font-style: italic;
    font-size: 15.5px;
    line-height: 20.5px;
    text-align: center;
    color: var(--ink);
  }
  .signatory {
    position: absolute;
    left: 492px;
    top: 620px;
    width: 250px;
    text-align: center;
  }
  .signature {
    display: block;
    font-family: "Mrs Saint Delafield", cursive;
    font-size: 52px;
    line-height: 62px;
    color: var(--ink);
    border-bottom: 1px solid var(--fill-line);
    padding-bottom: 4px;
  }
  .signatory-name {
    display: block;
    margin-top: 4px;
    font-family: "Pinyon Script", cursive;
    font-size: 30px;
    line-height: 36px;
    color: var(--ink);
  }
  .signatory-role {
    display: block;
    font-size: 16.5px;
    line-height: 22px;
    color: var(--ink);
  }
  .seal {
    position: absolute;
    left: 996px;
    top: 640px;
  }
</style>
</head>
<body>
<main class="certificate">

  <svg class="school-mark" width="1200" height="848" viewBox="0 0 1200 848" aria-hidden="true">
    <circle cx="805" cy="470" r="330" fill="var(--mark)"/>
    <circle cx="805" cy="470" r="225" fill="none" stroke="var(--mark-ring)" stroke-width="6"/>
  </svg>

  <svg class="title" width="1200" height="260" viewBox="0 0 1200 260">
    <path id="title-arc" d="M 385 160 Q 800 -40 1150 185" fill="none"/>
    <text><textPath href="#title-arc" textLength="790" lengthAdjust="spacingAndGlyphs">Certificate of Completion</textPath></text>
  </svg>

  <ul class="maxims">
    <li>This is Tidal Lotus</li>
    <li>Breath is primary</li>
    <li>Evolve the physical culture</li>
    <li class="two-line">Bring your unique<br>expression to the practice</li>
    <li>Take Breaks</li>
    <li>Freestyle</li>
    <li>Close your eyes</li>
    <li>Feel deeper into your body</li>
    <li>This is active meditation</li>
    <li>This is moving meditation</li>
    <li>This is modern meditation</li>
  </ul>

  <div class="divider"></div>

  <div class="brand">
    <span class="brand-dot"></span>
    <span class="brand-name">Tidal Lotus</span>
  </div>

  <p class="date-line">On this day <span class="blank day"></span> day of <span class="blank month"></span>,<span class="blank year"></span>.</p>

  <div class="name-line"></div>

  <p class="statement">has successfully completed the Tidal Lotus modern vinyasa yoga training, completing two hundred hours of instruction in practice and theory. Within the power of our institution as a certifying agent we declare Such-and-such, now, a teacher. competent to share the gift of yoga with the masses in a safe and effective</p>

  <div class="signatory">
    <span class="signature">D Halvorsen</span>
    <span class="signatory-name">Dennis Halvorsen</span>
    <span class="signatory-role">Tidal Lotus founder</span>
  </div>

  <svg class="seal" width="160" height="160" viewBox="0 0 160 160" role="img" aria-label="Red wax seal of the school">
    <defs>
      <radialGradient id="wax" cx="40%" cy="38%" r="65%">
        <stop offset="0%" stop-color="var(--seal-light)"/>
        <stop offset="60%" stop-color="var(--seal)"/>
        <stop offset="100%" stop-color="var(--seal-dark)"/>
      </radialGradient>
    </defs>
    <circle cx="80" cy="78" r="74" fill="url(#wax)"/>
  </svg>

</main>
</body>
</html>
```